Flyer needed for Seminar

Hello,
We are looking for eye-catching, inspiring marketing material for an educational seminar. We need 4 x 6 clubcards with the following info:

CLUBCARD FRONT:

Valtren Academy Presents:

Prayer: Past The Habit
Unlock the hidden treasures of prayer
By. Shaykh Idris Kamal Al-Tarifi

Dates:Jan 23-25, 2015
Timings: Fri - 7pm - 9:30 pm; Sat/Sun - 9am - 8 pm

Location: Dallas/Plano Corvane Suites at Ridgefield Commons
4830 Mercer Lane, Plano, TX 75093

Seating is Limited. Register Today!
www.ValtrenAcademy,example

CLUBCARD BACK:
In this unique seminar, learn how to connect spiritually with your Creator through prayer. Let us teach you the hidden meanings behind salah and why it is essential to your existence. Not only will the instructor impart the skills you'll need to master khushoo but he will delve more deeply, into the inner realms and intricacies of this ibadaa. As a result, the prayer will no longer be regarded as a mechanical chore, but an intimate meeting with the Divine. Through such insight, we hope you will leave this non-fiqh seminar with an awakened and unparalleled understanding of this fundamental pillar of Islam.

www.ValtrenAcademy.example
For more info: Email - info@valtrenacademy.example; Phone - 1-877-Valtren

Reason: I really appreciate all the submissions but am looking for something more eye-catching, something that really stirs ones interest and relates to the title of the seminar. Thank you!

```html
<!DOCTYPE html>
<html lang="en">
<head>
<meta charset="utf-8">
<title>Valtren Academy – Prayer: Past The Habit</title>
<link href="https://fonts.googleapis.com/css2?family=Libre+Franklin:wght@700;800;900&family=Arimo:ital,wght@0,700;1,700&display=swap" rel="stylesheet">
<style>
  :root {
    --page: #ffffff;
    --periwinkle: #a2b4de;
    --periwinkle-deep: #8fa6d6;
    --teal: #3e7d79;
    --gold: #f3c342;
    --gold-text: #f5c531;
    --ink: #111111;
    --white: #ffffff;
    --photo-sky: #f4f0ec;
    --photo-stone: #d9cfc6;
  }
  * { margin: 0; padding: 0; box-sizing: border-box; }
  html, body { width: 1200px; height: 914px; overflow: hidden; background: var(--page); }
  .sheet { position: relative; width: 1200px; height: 914px; }

  .card { position: absolute; top: 8px; height: 882px; background: var(--periwinkle); overflow: hidden; }
  .card--front { left: 8px; width: 592px; }
  .card--back { left: 611px; width: 582px; }

  .photo {
    position: absolute;
    background:
      radial-gradient(ellipse at 78% 22%, rgba(154,120,184,.85) 0%, rgba(154,120,184,0) 38%),
      radial-gradient(ellipse at 92% 70%, rgba(90,90,62,.55) 0%, rgba(90,90,62,0) 30%),
      linear-gradient(160deg, var(--photo-sky) 0%, var(--photo-stone) 55%, #c8bcb1 100%);
  }
  .card--front .photo { left: 0; top: 0; width: 592px; height: 430px; }
  .card--back .photo { left: 0; top: 168px; width: 582px; height: 714px; border-top-left-radius: 30px; }

  .date-badge {
    position: absolute; left: 8px; top: 8px; width: 140px; height: 140px; border-radius: 50%;
    background: var(--teal); color: var(--white);
    font-family: "Libre Franklin", Arial, sans-serif; font-weight: 800;
    display: flex; flex-direction: column; align-items: center; justify-content: center; line-height: 1.1;
  }
  .date-badge .month { font-size: 21px; }
  .date-badge .days { font-size: 23px; }
  .date-badge .year { font-size: 31px; }

  .presenter {
    position: absolute; left: 10px; top: 318px;
    font-family: "Libre Franklin", Arial, sans-serif; font-weight: 800; font-size: 45px; line-height: 1.08;
    color: var(--gold-text); text-shadow: 1px 2px 3px rgba(0,0,0,.45);
  }

  .title-block {
    position: absolute; left: 0; top: 430px; width: 560px; height: 140px;
    background: var(--periwinkle-deep); padding: 16px 14px 0 14px;
    font-family: "Libre Franklin", Arial, sans-serif; font-weight: 800; font-size: 27px; line-height: 1.3;
    color: var(--white);
  }
  .speaker {
    position: absolute; left: 14px; top: 592px;
    font-family: "Libre Franklin", Arial, sans-serif; font-weight: 700; font-size: 17px; color: var(--ink);
  }
  .timings {
    position: absolute; left: 14px; top: 622px;
    font-family: "Libre Franklin", Arial, sans-serif; font-weight: 700; font-size: 16px; line-height: 1.4; color: var(--ink);
  }
  .venue {
    position: absolute; left: 0; width: 592px; top: 768px; text-align: center;
    font-family: "Libre Franklin", Arial, sans-serif; font-weight: 800; color: var(--ink); line-height: 1.2;
  }
  .venue .place { font-size: 21px; }
  .venue .cta { font-size: 18px; }

  .contact-band {
    position: absolute; left: 0; top: 0; width: 582px; height: 168px; background: var(--gold);
    display: flex; flex-direction: column; justify-content: center; text-align: center;
    font-family: "Arimo", Arial, sans-serif; font-weight: 700; font-size: 18.5px; line-height: 1.22; color: var(--white);
  }
  .about {
    position: absolute; left: 148px; top: 212px; width: 440px; height: 552px;
    background: var(--periwinkle); border: 2px solid var(--ink); border-right: 0; border-top-left-radius: 28px;
    display: flex; align-items: center; padding: 0 26px 0 30px;
    font-family: "Arimo", Arial, sans-serif; font-weight: 700; font-style: italic; font-size: 16px; line-height: 1.55;
    color: var(--ink); text-align: center;
  }
</style>
</head>
<body>
<main class="sheet">
  <section class="card card--front">
    <div class="photo" role="img" aria-label="Photograph of a pale building facade framed by purple jacaranda blossoms"></div>
    <div class="date-badge">
      <span class="month">JANUARY</span>
      <span class="days">23-25th,</span>
      <span class="year">2015</span>
    </div>
    <h1 class="presenter">Valtren Academy<br>Presents:</h1>
    <h2 class="title-block">Prayer: Past The Habit<br>Unlock the hidden<br>treasures of prayer</h2>
    <p class="speaker">By. Shaykh Idris Kamal Al-Tarifi</p>
    <div class="timings">
      <p>Fri: 7pm – 9:30pm</p>
      <p>Sat/Sun: 9am – 8pm</p>
    </div>
    <div class="venue">
      <p class="place">Dallas/Plano Corvane Suites at Ridgefield Commons</p>
      <p class="place">4830 Mercer Lane, Plano, TX 75093</p>
      <p class="cta">Seating is Limited. Register Today!</p>
      <p class="cta">www.ValtrenAcademy,example</p>
    </div>
  </section>

  <section class="card card--back">
    <div class="contact-band">
      <p>Seating is Limited.</p>
      <p>Register Today!</p>
      <p>www.ValtrenAcademy.example</p>
      <p>For more info:</p>
      <p>Email - info@valtrenacademy.example;</p>
      <p>Phone - 1-877-Valtren</p>
    </div>
    <div class="photo" role="img" aria-label="Photograph of a pale building with purple jacaranda blossoms in the foreground"></div>
    <div class="about">
      <p>In this unique seminar, learn how to connect spiritually with your Creator through prayer. Let us teach you the hidden meanings behind salah and why it is essential to your existence. Not only will the instructor impart the skills you'll need to master khushoo but he will delve more deeply, into the inner realms and intricacies of this ibadaa. As a result, the prayer will no longer be regarded as a mechanical chore, but an intimate meeting with the Divine. Through such insight, we hope you will leave this non-fiqh seminar with an awakened and unparalleled understanding of this fundamental pillar of Islam.</p>
    </div>
  </section>
</main>
</body>
</html>
```